feld+klang
Zielgruppe
AUDIO-GUIDES FÜR DRAUSSEN, Entwicklung von Audio-Guides für Draußen
potentielle Auftraggeber: Standortmarketing, Tourismusmarketing, Gemeinden, Kulturinstitutionen
Aufgabenstellung
Layout Briefkopf /Visitenkarte
Text:
Feld und Klang (feld+klang)
AUDIO-GUIDES FÜR DRAUSSEN
www.feld-und-klang-beispiel.de
Visitenkarte Rückseite: Landschaften eine Stimme geben...
Das PDF zeigt einen ersten Versuch meinerseits, ich bin aber auch für ganz andere Vorschläge offen. Generell stelle ich mir eine schlichte Typographie vor, ohne Icons oder Ähnliches.

```html
<!DOCTYPE html>
<html lang="de">
<head>
<meta charset="utf-8">
<title>Feld und Klang – Visitenkarten</title>
<link rel="stylesheet" href="https://fonts.googleapis.com/css2?family=Questrial&family=Source+Sans+3:wght@400&display=swap">
<style>
  :root {
    --page: #f7f7f7;
    --card: #ffffff;
    --brand-red: #c1272d;
    --ink-grey: #666666;
    --ink-dark: #222222;
    --contact: #555555;
  }
  * { box-sizing: border-box; margin: 0; padding: 0; }
  html, body { width: 1200px; height: 1200px; overflow: hidden; background: var(--page); }
  .canvas { position: relative; width: 1200px; height: 1200px; }

  .card {
    position: absolute; width: 487px; height: 291px;
    background: var(--card);
    box-shadow: 5px 5px 6px rgba(0,0,0,0.55);
    overflow: hidden;
  }
  .card--front-a { left: 80px; top: 176px; }
  .card--back-a  { left: 651px; top: 176px; }
  .card--front-b { left: 80px; top: 635px; }
  .card--back-b  { left: 651px; top: 635px; }

  .wordmark {
    position: absolute; left: 54px; top: 28px;
    font-family: "Source Sans 3", sans-serif; font-weight: 400; font-size: 40px; line-height: 1;
    color: var(--ink-dark);
  }
  .tagline {
    position: absolute; left: 55px; top: 80px;
    font-family: "Source Sans 3", sans-serif; font-size: 17px; line-height: 1;
    color: var(--ink-grey); letter-spacing: 3px;
  }

  .contact {
    position: absolute;
    font-family: "Source Sans 3", sans-serif; font-size: 13.5px; line-height: 17.5px;
    color: var(--contact); font-style: normal; white-space: nowrap;
  }
  .contact--address { padding-left: 20px; }
  .contact--reach { padding-left: 21px; }
  .card--front-a .contact--address { left: 24px; top: 200px; }
  .card--front-a .contact--reach   { left: 255px; top: 215px; }
  .card--front-b .contact--address { left: 45px; top: 181px; }
  .card--front-b .contact--reach   { left: 276px; top: 196px; }

  .icon { position: absolute; fill: var(--contact); }
  .icon--house { left: 0; top: 18px; width: 16px; height: 15px; }
  .icon--phone { left: 0; top: 0; width: 15px; height: 17px; }
  .icon--mail  { left: 0; top: 22px; width: 14px; height: 10px; }

  .web-tab {
    position: absolute; background: var(--brand-red); color: #fff;
    font-family: "Source Sans 3", sans-serif; font-size: 12px;
    display: flex; align-items: center; gap: 8px; white-space: nowrap;
  }
  .web-tab--side {
    right: 0; top: 40px; width: 32px; height: 211px;
    border-radius: 16px 0 0 16px;
  }
  .web-tab--side .web-tab__inner {
    position: absolute; left: 50%; top: 50%;
    transform: translate(-50%, -50%) rotate(-90deg);
    display: flex; align-items: center; gap: 6px;
  }
  .web-tab--side .globe { transform: rotate(90deg); }
  .web-tab--bottom {
    left: 124px; bottom: 0; width: 240px; height: 32px;
    border-radius: 14px 14px 0 0; justify-content: center; font-size: 13px;
  }
  .globe { width: 14px; height: 14px; flex: none; }

  .claim { position: absolute; left: 0; top: 0; width: 100%; height: 100%; line-height: 1; }
  .claim span { position: absolute; white-space: nowrap; }
  .claim--round { font-family: "Questrial", sans-serif; font-size: 32px; color: var(--ink-dark); }
  .claim--round .claim__first  { left: 55px; top: 105px; }
  .claim--round .claim__second { left: 126px; top: 144px; }
  .claim--plain { font-family: "Source Sans 3", sans-serif; font-size: 30px; color: var(--ink-grey); letter-spacing: 1px; }
  .claim--plain .claim__first  { left: 38px; top: 114px; }
  .claim--plain .claim__second { left: 83px; top: 147px; }
</style>
</head>
<body>
<div class="canvas">

  <svg width="0" height="0" style="position:absolute">
    <defs>
      <symbol id="globe" viewBox="0 0 16 16">
        <g fill="none" stroke="#fff" stroke-width="1.2">
          <circle cx="8" cy="8" r="6.8"/>
          <ellipse cx="8" cy="8" rx="3" ry="6.8"/>
          <line x1="1.2" y1="8" x2="14.8" y2="8"/>
          <line x1="2.5" y1="4.5" x2="13.5" y2="4.5"/>
          <line x1="2.5" y1="11.5" x2="13.5" y2="11.5"/>
        </g>
      </symbol>
      <symbol id="house" viewBox="0 0 16 15">
        <path d="M8 0 L16 7.5 L14 7.5 L14 15 L10 15 L10 10 L6 10 L6 15 L2 15 L2 7.5 L0 7.5 Z"/>
      </symbol>
      <symbol id="phone" viewBox="0 0 15 17">
        <path d="M11 0 L15 2 L13.5 4.5 L11.5 3.5 C9 5 6 9 5.5 12.5 L7.5 13.5 L6 17 L3 15.5 C2 11 6 3.5 11 0 Z"/>
      </symbol>
      <symbol id="mail" viewBox="0 0 14 10">
        <path d="M0 0 H14 V10 H0 Z M1.5 1 L7 5.5 L12.5 1 Z M1 2 V9 L5 5.2 Z M13 2 V9 L9 5.2 Z M1.8 9 H12.2 L8.3 6 L7 7 L5.7 6 Z" fill-rule="evenodd"/>
      </symbol>
    </defs>
  </svg>

  <section class="card card--front-a">
    <div class="wordmark">Feld und Klang</div>
    <div class="tagline">AUDIO-GUIDES FÜR DRAUSSEN</div>
    <address class="contact contact--address">
      <svg class="icon icon--house"><use href="#house"/></svg>
      Mara Lumbrek,<br>Lindenweg 14,<br>12345 Musterhausen-Talfeld
    </address>
    <div class="contact contact--reach">
      <svg class="icon icon--phone"><use href="#phone"/></svg>
      <svg class="icon icon--mail"><use href="#mail"/></svg>
      49 170 0000000<br>mara@fk-beispiel.de
    </div>
    <div class="web-tab web-tab--side">
      <div class="web-tab__inner">
        <svg class="globe"><use href="#globe"/></svg>
        <span>www.feld-und-klang-beispiel.de</span>
      </div>
    </div>
  </section>

  <section class="card card--back-a">
    <p class="claim claim--round">
      <span class="claim__first">Landschaften</span>
      <span class="claim__second">eine Stimme geben...</span>
    </p>
  </section>

  <section class="card card--front-b">
    <div class="wordmark">Feld und Klang</div>
    <div class="tagline">AUDIO-GUIDES FÜR DRAUSSEN</div>
    <address class="contact contact--address">
      <svg class="icon icon--house"><use href="#house"/></svg>
      Mara Lumbrek,<br>Lindenweg 14,<br>12345 Musterhausen-Talfeld
    </address>
    <div class="contact contact--reach">
      <svg class="icon icon--phone"><use href="#phone"/></svg>
      <svg class="icon icon--mail"><use href="#mail"/></svg>
      49 170 0000000<br>mara@fk-beispiel.de
    </div>
    <div class="web-tab web-tab--bottom">
      <svg class="globe"><use href="#globe"/></svg>
      <span>www.feld-und-klang-beispiel.de</span>
    </div>
  </section>

  <section class="card card--back-b">
    <p class="claim claim--plain">
      <span class="claim__first">Landschaften</span>
      <span class="claim__second">eine Stimme geben...</span>
    </p>
  </section>

</div>
</body>
</html>
```